website for local kavenda practicioner and yoga teacher trainer

The website should function primarily as:
A place where people can discover Kavenda and book sessions.
A central hub connecting all of my work.
A professional home that reflects my personality and approach.
Website design for Liesbet Oonwerk — Kavenda® Structural Integration practitioner, movement educator, yoga teacher and teacher trainer.
A website that can grow with future projects.
The website should feel: Warm, Human, Invitational, Professional, Accessible, Intelligent, Calm, Clear, Playful, Exploratory, Trustworthy
Avoid: New age aesthetics, Mystical clichés, Excessive spirituality, ”Guru" vibes, Overly clinical design, Corporate wellness branding, Busy layouts
Think: modern, grounded, curious and real.
My work combines three interconnected areas:
1.Bodywork: Touch, structure, awareness and one-on-one support.
2. Movement: Yoga, Pilates and embodied movement.
3. Education: Teacher trainings, workshops and continued learning.
Underlying values:
Curiosity over certainty
Possibility over perfection
Complexity without overwhelm
Science and lived experience together
Exploration rather than dogma
Human beings before methods
The primary goal of the website is to introduce people to Kavenda® Structural Integration and make it easy for them to:
Understand what Kavenda is
Discover whether it might be relevant for them
Learn what to expect from a session
Book an appointment
Booking should always feel visible and easy.
Secondary Goal: Present all other aspects of my work in one coherent place:
Yoga classes
Pilates classes
Teacher trainings
Workshops
Retreats
One-on-one movement sessions
Collaborations with studios
Website Structure
1: HOME
1.1.Hero Section: Large welcoming image
1.2 Two Main Pathways
- Bodywork: Kavenda® Structural Integration
- Movement & Education: Yoga, Pilates, trainings, workshops and retreats
- About Preview: Small introduction with portrait. + Button:
Read More
1.3 Current Events / What's Coming Up: Upcoming trainings, workshops and retreats. (This section should be easy to update)
1.4. Contact / Newsletter: Simple contact information
2: Kavenda® Structural Integration
What is Kavenda?
For whom is it?
What does a session look like?
FAQ
Prices
Booking
Future possibility:
Kaven Movement sessions
3: Movement
- Introductory text.
- Studio Classes (link to “my home base” - > local yoga studio)
- One-to-One Sessions: booking option (this is small; not a key aspect I want to promote)
- Workshops/ Retreats / Teacher Trainings => This section should be flexible and easy to update. Visitors should be able to click into specific offerings.
4. Events
Dynamic page for: Teacher trainings, Retreats, Workshops (see section in movement; here more elaborate)
Each event should contain: Image, Short description, Location, Date, Button for more information. (Linking to hosting studio/location)
5. Work With Me
For studios, organisations and teacher training schools.
Examples: Guest teaching, Workshops, Anatomy, Sequencing, Teacher development , Continuing education -> Clear call-to-action.
Call to action!!=> Book a Session
Prominent button in the navigation.
Footer:
- About Me: Longer biography (6th page)
Personal story and background.
- Testimonials (7th page): Separate page containing testimonials from:
Kavenda clients
Students
Teacher trainees
- Contact: 8th page
Visual Direction
Natural textures. Lots of white space.Editorial feeling.Professional photography.Simple navigation.
Less "wellness influencer.” More:Thoughtful, Contemporary, Timeless, Grounded, Human
Photography should show:
Teaching
Hands-on work
Natural movement
Real interaction
Simplicity
Avoid stereotypical yoga imagery and overly spiritual aesthetics.
Keywords
Warm. Curious. Human. Professional. Embodied. Intelligent. Accessible. Playful. Grounded. Exploratory. Real.
Inspiration / Core Message
Helping people feel more at home in their bodies through touch, movement and education.
The website should communicate that these are not separate services, but different expressions of the same intention:
Bodywork • Movement • Education.
Colours:
light orange/beige: e3d5c4
light orange/off white: f9f7f3
gray azure: 556b78
orange: d07b5a
grey orange: c09f80
dark grey: 3e3e3e
dark gray cyan 2f4f4f
gray green colour: a7c4a0
Fonts: Montserrat and Poppins + raleway
In added documents a try out idea of a website + logo. I will mainly use the logo with diffrent colours (image next to text).
My audience consists of people who want to feel more at home in their bodies and who appreciate a thoughtful, grounded and human approach to movement, touch and education. (30-65yo)
wellbeing
5+ page
- montserrat, poppins, raleway

```html
<!DOCTYPE html>
<html lang="en">
<head>
<meta charset="utf-8">
<title>Liesbet Oonwerk — Yoga &amp; Bodywork</title>
<link href="https://fonts.googleapis.com/css2?family=Montserrat:ital,wght@0,400;0,500;0,600;1,400;1,600&family=Poppins:wght@400;500;600&family=Raleway:ital,wght@0,400;0,500;0,600;1,500;1,600;1,700&display=swap" rel="stylesheet">
<style>
:root{
  --beige:#e3d5c4;
  --offwhite:#f9f7f3;
  --azure:#556b78;
  --orange:#d07b5a;
  --orange-bright:#e67e57;
  --grey-orange:#c09f80;
  --dark:#3e3e3e;
  --cyan-dark:#2f4f4f;
  --green:#a7c4a0;
  --card-peach:#e8a78d;
  --card-slate:#95a6ae;
  --text:#3e3e3e;
  --white:#ffffff;
}
*{box-sizing:border-box;margin:0;padding:0}
html,body{width:1200px;height:4464px;overflow:hidden}
body{background:var(--white);font-family:"Montserrat",sans-serif;color:var(--text);position:relative}
section,header,footer{position:absolute;left:0;width:1200px}
.btn{display:inline-flex;align-items:center;justify-content:space-between;gap:18px;font-family:"Poppins",sans-serif;font-size:11px;font-weight:500;color:var(--white);border-radius:20px;height:36px;padding:0 16px 0 30px;text-decoration:none;white-space:nowrap}
.btn::after{content:"";width:6px;height:6px;border-radius:50%;background:currentColor}
.btn-orange{background:var(--orange-bright)}
.btn-green{background:var(--green)}
.accent{font-style:italic;font-weight:600}
.accent-orange{color:var(--orange-bright);font-style:italic}
.photo{position:absolute;overflow:hidden}

/* Header */
.site-header{top:0;height:80px;z-index:5}
.brand{position:absolute;left:130px;top:24px;display:flex;align-items:center;gap:10px;font-family:"Raleway",sans-serif;font-weight:500;font-size:22px;color:var(--white);text-decoration:none}
.brand-dot{width:24px;height:24px;border-radius:50%;background:var(--white)}
.main-nav{position:absolute;left:416px;top:33px;display:flex;gap:13px;font-size:8.5px;color:var(--white);white-space:nowrap}
.main-nav a{color:inherit;text-decoration:none}
.nav-book{position:absolute;left:944px;top:21px;height:36px;border:1.5px solid var(--white);background:transparent;font-size:10px}

/* Hero */
.hero{top:0;height:720px}
.hero-bg{position:absolute;inset:0}
.hero-photo{left:580px;top:135px;width:540px;height:540px;border-radius:50%;border:9px solid var(--white);background:radial-gradient(circle at 55% 40%,#d8a089,#b5533f 45%,#8d8b86 75%,#c8c4bc)}
.hero-badge{position:absolute;left:132px;top:210px;background:rgba(255,255,255,.12);color:var(--white);font-size:9px;font-weight:600;padding:6px 24px;border-radius:12px}
.hero h1{position:absolute;left:130px;top:240px;font-family:"Raleway",sans-serif;font-weight:500;font-size:38px;line-height:44px;color:var(--white)}
.hero-lead{position:absolute;left:132px;top:386px;width:400px;font-size:12.5px;line-height:19px;color:var(--white)}
.hero-actions{position:absolute;left:130px;top:443px;display:flex;gap:6px}
.hero-dots{position:absolute;left:148px;top:507px;display:flex;gap:5px}
.hero-dots span{width:10px;height:10px;border-radius:50%;border:1px solid var(--white)}
.hero-dots span.on{background:var(--white)}

/* Intro */
.intro{top:720px;height:643px}
.intro-photo{left:194px;top:156px;width:358px;height:428px;border-radius:0 0 180px 180px;background:linear-gradient(160deg,#c9a391,#e6c2b4 45%,#d49182 75%,#e9d4cb)}
.intro-badge{position:absolute;left:481px;top:272px;width:114px;height:114px;border-radius:50%;background:var(--white);border:3px solid var(--azure);box-shadow:0 0 0 6px var(--white)}
.intro-text{position:absolute;left:630px;top:196px;width:420px;font-style:italic;font-size:12.5px;line-height:19px}
.intro-text p{margin-bottom:19px}

/* Pathways */
.pathways{top:1363px;height:615px}
.pathways-bg{position:absolute;inset:0;background:linear-gradient(90deg,#f3f1ee 0%,#eeeae6 55%,#d9c6b3 70%,#9f8f86 85%,#6f6a69 100%)}
.pathways h2{position:absolute;top:80px;width:1200px;text-align:center;font-family:"Raleway",sans-serif;font-weight:500;font-size:31px;color:var(--dark)}
.path-card{position:absolute;top:189px;width:266px;height:314px;border-radius:18px;padding:28px 28px;color:var(--white)}
.path-card.bodywork{left:132px;background:var(--card-peach)}
.path-card.movement{left:411px;background:var(--card-slate)}
.path-card .kicker{font-size:11px;margin-bottom:6px}
.path-card h3{font-family:"Raleway",sans-serif;font-weight:500;font-size:14px;margin-bottom:12px;white-space:nowrap}
.path-card p{font-size:8.5px;line-height:13px;margin-bottom:8px;opacity:.95}
.path-card .btn{position:absolute;left:32px;bottom:28px;height:34px;font-size:10px}

/* About */
.about{top:1978px;height:635px}
.about-blob{position:absolute;left:120px;top:110px;width:300px;height:320px;background:#d9d9d9;border-radius:50% 40% 50% 45%}
.about-pink{position:absolute;left:290px;top:390px;width:90px;height:70px;background:#f2ccc0;border-radius:50%}
.about-dot{position:absolute;left:276px;top:90px;width:56px;height:56px;border-radius:50%;background:#c6d2d9}
.about-photo-main{left:184px;top:112px;width:336px;height:336px;border-radius:50%;background:linear-gradient(135deg,#8c7e74,#d3c3b6 45%,#f0ebe5 70%,#b8a99b)}
.about-photo-small{left:356px;top:330px;width:212px;height:212px;border-radius:50%;border:7px solid var(--white);background:linear-gradient(140deg,#cfc7bd,#8b4a3d 45%,#9a9288 80%)}
.about-text{position:absolute;left:647px;top:146px;width:370px}
.about-text h2{font-family:"Raleway",sans-serif;font-weight:500;font-size:30px;margin-bottom:20px}
.about-text h2 .accent-orange{font-weight:600}
.about-text p{font-size:10.5px;line-height:15px;margin-bottom:10px}
.about-text .langs{font-style:italic;font-weight:600;margin:22px 0 18px}
.about-text .btn{height:36px}

/* Events */
.events{top:2613px;height:673px;background:var(--grey-orange)}
.events h2{position:absolute;top:64px;width:1200px;text-align:center;font-family:"Raleway",sans-serif;font-weight:500;font-size:31px;color:var(--white)}
.event-card{position:absolute;top:139px;width:282px;height:404px;background:var(--white);border-radius:16px;overflow:hidden}
.event-card:nth-of-type(1){left:156px}
.event-card:nth-of-type(2){left:448px}
.event-card:nth-of-type(3){left:740px}
.event-image{height:180px}
.event-body{padding:28px 34px}
.event-body .status{font-size:9.5px;color:var(--orange-bright);margin-bottom:12px}
.event-body h3{font-family:"Raleway",sans-serif;font-weight:500;font-size:15px;line-height:19px;margin-bottom:12px}
.event-body p{font-size:8.5px;line-height:13px;margin-bottom:20px;min-height:52px}
.event-body .btn{height:36px;font-size:10px;padding-left:34px}

/* Connect */
.connect{top:3286px;height:636px}
.connect-photo{position:absolute;left:968px;top:58px;width:232px;height:714px;border-radius:120px 0 100px 120px;background:linear-gradient(180deg,#d9a283 0%,#2b2b2b 22%,#e9c5b0 45%,#202020 65%,#2a2a2a 100%);z-index:3}
.connect h2{position:absolute;width:1200px;text-align:center;font-family:"Raleway",sans-serif;font-weight:500;color:var(--dark)}
.connect p.center{position:absolute;width:1200px;text-align:center;font-size:10.5px;line-height:16px}
.newsletter-form{position:absolute;left:360px;top:184px;width:476px;height:36px;border:1px solid #e6e0da;border-radius:18px;display:flex;align-items:center;justify-content:space-between;padding-left:30px;font-size:9.5px;color:#a7a7a7}
.newsletter-form .btn{height:36px;padding:0 30px;font-size:9.5px}
.newsletter-form .btn::after{display:none}
.contact-item{position:absolute;top:526px;display:flex;align-items:center;gap:16px;font-size:11px;line-height:17px;white-space:nowrap}
.contact-item.email{left:265px}
.contact-item.phone{left:508px}
.contact-item.location{left:722px}
.contact-item strong{font-weight:500;display:block}
.contact-icon{width:54px;height:54px;border-radius:50%;border:1.5px solid #f1c9b6;display:flex;align-items:center;justify-content:center}

/* Footer */
.site-footer{top:3922px;height:542px;background:var(--dark);color:var(--white)}
.footer-brand{position:absolute;left:143px;top:248px;display:flex;align-items:center;gap:12px;font-family:"Raleway",sans-serif;font-weight:500;font-size:36px}
.footer-brand .brand-dot{width:44px;height:44px}
.footer-links{position:absolute;top:218px;list-style:none;font-size:12.5px;line-height:25px}
.footer-links a{color:var(--white)}
.footer-links.primary{left:525px}
.footer-links.legal{left:775px}
.footer-social{position:absolute;left:955px;top:208px;list-style:none}
.footer-social li{display:flex;align-items:center;gap:12px;font-size:12.5px;margin-bottom:8px}
.footer-social span.circle{width:34px;height:34px;border-radius:50%;background:#5a5a5a}
.footer-rule{position:absolute;left:132px;top:476px;width:936px;height:1px;background:#6a6a6a}
.copyright{position:absolute;left:460px;top:496px;font-size:11px}
.copyright strong{font-family:"Raleway",sans-serif;font-weight:600;font-size:14px}
.footer-tagline{position:absolute;left:866px;top:497px;font-size:11px}
.to-top{position:absolute;left:1111px;top:460px;width:42px;height:42px;border-radius:50%;background:var(--orange-bright);display:flex;align-items:center;justify-content:center}
</style>
</head>
<body>

<header class="site-header">
  <a class="brand" href="#"><span class="brand-dot"></span>Liesbet Oonwerk</a>
  <nav class="main-nav">
    <a href="#">Kavenda Structural Integration</a>
    <a href="#">Movement</a>
    <a href="#">Events</a>
    <a href="#">Work With Me</a>
    <a href="#">About Me</a>
    <a href="#">Testimonials</a>
    <a href="#">Contact</a>
  </nav>
  <a class="btn nav-book" href="#">Book a Session</a>
</header>

<section class="hero">
  <svg class="hero-bg" width="1200" height="720" viewBox="0 0 1200 720" role="img" aria-label="Soft background photo of a movement class, tinted blue">
    <defs>
      <linearGradient id="heroTint" x1="0" y1="0" x2="1" y2="1">
        <stop offset="0" stop-color="#5f7886"/>
        <stop offset="1" stop-color="#4d6370"/>
      </linearGradient>
    </defs>
    <rect width="1200" height="720" fill="url(#heroTint)"/>
    <path d="M790 0 H1200 V720 C1150 660 1110 640 1080 600 C1180 500 1170 280 1040 160 C960 90 880 40 790 0 Z" fill="#e67e57"/>
    <path d="M0 560 C200 600 420 560 640 520 C820 490 980 560 1200 720 L0 720 Z" fill="#e3d5c4"/>
    <path d="M0 700 C220 650 440 610 660 590 C860 575 1020 620 1200 720 L0 720 Z" fill="#e67e57"/>
    <path d="M0 720 L0 716 C240 680 460 650 680 640 C880 632 1040 668 1200 720 Z" fill="#ffffff"/>
  </svg>
  <div class="photo hero-photo" role="img" aria-label="Photo of a teacher guiding a student through a standing arm stretch in a bright studio"></div>
  <span class="hero-badge">Welcome To Liesbet Oonwerk</span>
  <h1>Yoga and bodywork<br>For more ease, <span class="accent">resilience,</span><br>and connection.</h1>
  <p class="hero-lead">Helping people feel more at home in their bodies through touch, movement, and education.</p>
  <div class="hero-actions">
    <a class="btn btn-orange" href="#">Book a Session</a>
    <a class="btn btn-green" href="#">Discover My Approach</a>
  </div>
  <div class="hero-dots"><span></span><span class="on"></span><span></span><span></span></div>
</section>

<section class="intro">
  <div class="photo intro-photo" role="img" aria-label="Photo of two women leaning into each other in a partner stretch"></div>
  <span class="intro-badge"></span>
  <div class="intro-text">
    <p>At the heart of my work is the belief that our bodies are not machines to optimise, but living, sensing systems full of intelligence, adaptability, and possibility.</p>
    <p>Through movement, breath, touch, and attention, we can build greater capacity, support, grounding, and ease — not by forcing ourselves into fixed shapes or ideals, but by learning to listen more closely to the body and its changing needs.</p>
    <p>From this place of connection, new possibilities for movement, expression, and being begin to open up. We find not a single “better” way to move or live, but more freedom, responsiveness, and choice.</p>
  </div>
</section>

<section class="pathways">
  <div class="pathways-bg" role="img" aria-label="Photo of one woman comforting another, both seated on white chairs"></div>
  <h2>Where would <span class="accent">you</span> <span class="accent-orange">like</span> to begin?</h2>
  <article class="path-card bodywork">
    <div class="kicker">Bodywork</div>
    <h3>Kavenda Structural Integration</h3>
    <p>A collaborative process exploring posture, movement, breath, and relationship to gravity through touch, awareness, and movement.</p>
    <p>Sessions invite greater ease, support, adaptability, and resilience — not by “fixing” the body, but by creating space for new patterns, perceptions, and possibilities to emerge.</p>
    <p>Work takes place mostly on a treatment table, sometimes through standing or movement exploration.</p>
    <a class="btn btn-green" href="#">Learn More About Kavenda</a>
  </article>
  <article class="path-card movement">
    <div class="kicker">Movement</div>
    <h3>Yoga, Pilates &amp; Education</h3>
    <p>Movement as exploration — a space to build strength, mobility, awareness, resilience, and a little more freedom in how we move and relate to ourselves.</p>
    <p>Classes weave together breath, anatomy, playfulness, challenge, rest, and attention.</p>
    <p>Group classes, private sessions, trainings, and retreats.</p>
    <a class="btn btn-green" href="#">Explore Classes &amp; Trainings</a>
  </article>
</section>

<section class="about">
  <span class="about-blob"></span>
  <span class="about-pink"></span>
  <span class="about-dot"></span>
  <div class="photo about-photo-main" role="img" aria-label="Photo of a hands-on bodywork session on a mat"></div>
  <div class="photo about-photo-small" role="img" aria-label="Photo of a teacher and student practising arm movements together"></div>
  <div class="about-text">
    <h2>About <span class="accent-orange">Liesbet</span></h2>
    <p>"My background in contemporary dance, Pilates, and yoga shape how I move, teach, touch, and relate to people.</p>
    <p>What connects them is curiosity: the body is not something to perfect or control, but something to listen to, to explore, and live within. Every body carries stories, habits, tensions, and possibilities — and every story moves.</p>
    <p>Based in Leiden, I offer group classes, trainings, retreats, and one-on-one sessions in movement and bodywork, both locally and abroad.</p>
    <p class="langs">I work in English, Dutch, and French."</p>
    <a class="btn btn-orange" href="#">Read More About Us</a>
  </div>
</section>

<section class="events">
  <h2>Upcoming Trainings, <span class="accent">Workshops</span> &amp; Retreats</h2>
  <article class="event-card">
    <div class="event-image" role="img" aria-label="Photo of a teacher leading a workshop in a brick-walled studio" style="background:linear-gradient(135deg,#8a4a34,#c9866a 50%,#6f5a4d)"></div>
    <div class="event-body">
      <div class="status">Coming Autumn 2026</div>
      <h3>Anatomy &amp; Embodied Sequencing</h3>
      <p>A practical exploration combining science and lived experience to enhance your teaching development and movement sequencing.</p>
      <a class="btn btn-orange" href="#">View Details</a>
    </div>
  </article>
  <article class="event-card">
    <div class="event-image" role="img" aria-label="Photo of a quiet garden path lined with trees" style="background:linear-gradient(135deg,#4f5e4a,#9aa59a 50%,#6b7a55)"></div>
    <div class="event-body">
      <div class="status">Coming Soon</div>
      <h3>Grounded Living Movement Retreat</h3>
      <p>Step away to explore touch, structure, and awareness. A dedicated space to feel more at home in your body.</p>
      <a class="btn btn-orange" href="#">Learn More</a>
    </div>
  </article>
  <article class="event-card">
    <div class="event-image" role="img" aria-label="Photo of a table with tea, snacks and study books" style="background:linear-gradient(135deg,#3a2a22,#b87a4f 50%,#d8cfc4)"></div>
    <div class="event-body">
      <div class="status">Registration Opening Soon</div>
      <h3>Teacher Training &amp; Advanced Mentorship</h3>
      <p>Deepen your expertise with continuing education workshops focusing on complexity without overwhelm and somatic intelligence.</p>
      <a class="btn btn-orange" href="#">Join Waitlist</a>
    </div>
  </article>
</section>

<section class="connect">
  <div class="connect-photo" role="img" aria-label="Photo of a practitioner giving a seated assisted stretch to a client"></div>
  <h2 style="top:92px;font-size:33px">Newsletter</h2>
  <p class="center" style="top:142px">Receive occasional updates about upcoming events, trainings and offerings.</p>
  <div class="newsletter-form">you@example.com<span class="btn btn-orange">Subscribe</span></div>
  <h2 style="top:268px;font-size:21px">Prefer to begin with a session?</h2>
  <a class="btn btn-orange" href="#" style="position:absolute;left:522px;top:313px">Book a Session</a>
  <h2 style="top:402px;font-size:31px">Stay Connected</h2>
  <p class="center" style="top:461px">For questions, booking inquiries or updates about upcoming workshops, trainings &amp;<br>retreats, feel free to get in touch.</p>
  <div class="contact-item email">
    <span class="contact-icon"><svg width="16" height="12" viewBox="0 0 16 12"><rect width="16" height="12" rx="1.5" fill="#e67e57"/><path d="M1 1.5 8 7l7-5.5" stroke="#fff" stroke-width="1.4" fill="none"/></svg></span>
    <div><strong>Email Address:</strong>hello@liesbetoonwerk.com</div>
  </div>
  <div class="contact-item phone">
    <span class="contact-icon"><svg width="16" height="16" viewBox="0 0 24 24"><path d="M6.6 10.8a15 15 0 0 0 6.6 6.6l2.2-2.2c.3-.3.7-.4 1-.2 1.1.4 2.3.6 3.6.6.6 0 1 .4 1 1V20c0 .6-.4 1-1 1A17 17 0 0 1 3 4c0-.6.4-1 1-1h3.5c.6 0 1 .4 1 1 0 1.3.2 2.5.6 3.6.1.3 0 .7-.2 1z" fill="#e67e57"/></svg></span>
    <div><strong>Phone Number:</strong>+32 (0)470 18 62 09</div>
  </div>
  <div class="contact-item location">
    <span class="contact-icon"><svg width="14" height="18" viewBox="0 0 14 18"><path d="M7 0a7 7 0 0 0-7 7c0 5 7 11 7 11s7-6 7-11a7 7 0 0 0-7-7z" fill="#e67e57"/><circle cx="7" cy="7" r="2.5" fill="#fff"/></svg></span>
    <div><strong>Location:</strong>Belgium · By appointment</div>
  </div>
</section>

<footer class="site-footer">
  <div class="footer-brand"><span class="brand-dot"></span>Liesbet Oonwerk</div>
  <ul class="footer-links primary">
    <li><a href="#">Home</a></li>
    <li><a href="#">Kavenda Structural Integration</a></li>
    <li><a href="#">Movement</a></li>
    <li><a href="#">Events</a></li>
    <li><a href="#">Work With Me</a></li>
    <li><a href="#">About Me</a></li>
    <li><a href="#">Testimonials</a></li>
    <li><a href="#">Contact</a></li>
  </ul>
  <ul class="footer-links legal">
    <li><a href="#">Terms &amp; Condition</a></li>
    <li><a href="#">Privacy policy</a></li>
    <li><a href="#">Contact</a></li>
  </ul>
  <ul class="footer-social">
    <li><span class="circle"></span>Circlepage</li>
    <li><span class="circle"></span>Chirpline</li>
    <li><span class="circle"></span>Workgraph</li>
  </ul>
  <div class="footer-rule"></div>
  <p class="copyright">© 2025 <strong>Liesbet Oonwerk.</strong> - All rights reserved</p>
  <p class="footer-tagline">Bodywork · Movement · Education</p>
  <a class="to-top" href="#" aria-label="Back to top"><svg width="12" height="12" viewBox="0 0 12 12"><path d="M6 11V1M1.5 5.5 6 1l4.5 4.5" stroke="#fff" stroke-width="1.5" fill="none"/></svg></a>
</footer>

</body>
</html>
```